Introducing Us/Sales Person - Sales Flyer

We are a business which manufactures and sells Blinds, Awnings, Curtains, Security Doors. We have sales people driving to customers homes all day every day. The sales team have asked for a small flyer they can give to people they see as they travel or drop into the letterbox of next door neighbors.

I would like a design of a flyer that is upmarket and professional.

It should include information about the business, what products we do and our contact information. It should also introduce the consultant and a small bio on them.

The design must compliment our design bible guidelines and other marketing materials that are attached in a PDF to this document. You can access the design bible here - **removed**
The flyers will be purchased through either https://www.paperkite.com.au/marketing-materials/flyers or http://www.quillmerepress.com.au/quick-flyers-postcards-brochures-printing.htm. You have creative freedom on the shape and design but remember it needs to be professional, not just a cheap looking a4 page. One option would be a door hanger (https://www.paperkite.com/marketing-materials/door-hangers) although don't restrict yourself to this design format.

Example Content - You can use this or modify it - changing its length, tone or anything you like -

Sales Consultant - Ross Melvane

Ross has been involved in the Blind, Awning & Security Industry for over 40 years with extensive knowledge in both modern and traditional methods of covering doors, windows and outdoor areas.

With a keen eye for symmetry and aesthetics, Ross is able to help customers cut through the many options to the product which will work for their needs and look great in their home.

Ross has an interest in renovating homes with some of his past projects featured in magazines showing that under the sometimes rough exterior is a fine attention to detail and the skill to make your home stand out.

Trained in all our product areas and able to work through even the most complex jobs; he is available to come to your home at a convenient time and help you 'rest easy' with the addition of Wexley Hart products.

Company Info -

Use our website, examples brochures and the letter attached to steal some appropriate content.

Target Market(s)

Customers aged 35-55
Slightly female focussed

Industry/Entity Type

Home Improvement

Font styles to use
Other font styles liked:
• Gotham

Colors

Designer to choose colors to be used in the design.

Requirements
Must have
• Quality Design
• Appropriate with our logo and other marketing design work
• Professional Look
Nice to have
• Couple of layout options? Maybe door hanger or standard flyer?

```html
<!DOCTYPE html>
<html lang="en">
<head>
<meta charset="utf-8">
<title>Ross Melvane – Door Hanger</title>
<link href="https://fonts.googleapis.com/css2?family=Raleway:wght@400;500;700;800&display=swap" rel="stylesheet">
<style>
  :root {
    --teal: #2f97b5;
    --teal-deep: #227f9c;
    --ink: #4a4f55;
    --muted: #8a9096;
    --paper: #ffffff;
    --stage: #e9edf0;
    --edge: #c9ced3;
  }
  html, body {
    margin: 0;
    width: 1200px;
    height: 960px;
    overflow: hidden;
    background: var(--stage);
    font-family: "Raleway", sans-serif;
  }
  .hanger {
    position: absolute;
    left: 390px;
    top: 20px;
    width: 420px;
    height: 920px;
    filter: drop-shadow(0 10px 24px rgba(0,0,0,0.18));
  }
  .hanger-shape { position: absolute; inset: 0; }
  .consultant-photo {
    position: absolute;
    left: 38px;
    top: 262px;
    width: 104px;
    height: 116px;
    background: linear-gradient(160deg, #3a8ea8, #5a6770);
    border-radius: 3px;
  }
  .consultant-heading {
    position: absolute;
    left: 156px;
    top: 282px;
  }
  .consultant-name {
    margin: 0;
    font-size: 30px;
    font-weight: 800;
    color: var(--teal);
    line-height: 1;
  }
  .consultant-role {
    margin: 6px 0 0 70px;
    font-size: 13px;
    color: var(--muted);
  }
  .bio {
    position: absolute;
    left: 38px;
    top: 392px;
    width: 344px;
    color: var(--ink);
    font-size: 13px;
    line-height: 17.5px;
    text-align: justify;
  }
  .bio p { margin: 0 0 11px; }
  .contact {
    position: absolute;
    left: 48px;
    top: 812px;
    margin: 0;
    padding: 0;
    list-style: none;
    color: #fff;
    font-size: 15px;
    line-height: 21px;
  }
  .contact li { display: flex; align-items: flex-start; gap: 12px; }
  .contact svg { width: 16px; height: 16px; margin-top: 3px; flex: none; }
</style>
</head>
<body>
  <div class="hanger">
    <svg class="hanger-shape" width="420" height="920" viewBox="0 0 420 920">
      <defs>
        <mask id="hanger-cut">
          <rect width="420" height="920" rx="28" fill="#fff"/>
          <circle cx="200" cy="170" r="66" fill="#000"/>
          <path d="M214 108 L244 0 L266 0 L236 112 Z" fill="#000"/>
        </mask>
      </defs>
      <g mask="url(#hanger-cut)">
        <rect width="420" height="920" fill="var(--paper)"/>
        <path class="top-band" d="M0 0 H420 V70 C300 80 60 150 0 300 Z" fill="var(--teal)"/>
        <path d="M0 300 C60 150 300 80 420 70 V84 C300 96 80 170 0 320 Z" fill="var(--edge)" opacity="0.5"/>
        <path d="M0 778 C170 782 340 752 420 672 V920 H0 Z" fill="var(--edge)"/>
        <path class="bottom-band" d="M0 792 C170 796 340 766 420 690 V920 H0 Z" fill="var(--teal)"/>
      </g>
    </svg>

    <div class="consultant-photo" role="img" aria-label="Portrait photo of sales consultant Ross Melvane"></div>
    <div class="consultant-heading">
      <h1 class="consultant-name">Ross Melvane</h1>
      <p class="consultant-role">Sales Consultant</p>
    </div>

    <div class="bio">
      <p>Ross has been involved in the Blind, Awning &amp; Security Industry for over 40 years with extensive knowledge in both modern and traditional methods of covering doors, windows and outdoor areas.</p>
      <p>With a keen eye for symmetry and aesthetics, Ross is able to help customers cut through the many options to the product which will work for their needs and look great in their home.</p>
      <p>Ross has an interest in renovating homes with some of his past projects featured in magazines showing that under the sometimes rough exterior is a fine attention to detail and the skill to make your home stand out.</p>
      <p>Trained in all our product areas and able to work through even the most complex jobs; he is available to come to your home at a convenient time and help you 'rest easy' with the addition of Wexley Hart products.</p>
    </div>

    <ul class="contact">
      <li>
        <svg viewBox="0 0 16 16"><path d="M8 1a5 5 0 0 0-5 5c0 4 5 9 5 9s5-5 5-9a5 5 0 0 0-5-5zm0 7a2 2 0 1 1 0-4 2 2 0 0 1 0 4z" fill="#fff"/></svg>
        <span>7/214 Harrowgate Rd<br>Kelmsford SA 5081</span>
      </li>
      <li>
        <svg viewBox="0 0 16 16"><circle cx="8" cy="8" r="7" fill="none" stroke="#fff" stroke-width="1.4"/><path d="M5.5 4.5l1.5 1.5-1 1c.6 1.2 1.5 2.1 2.7 2.7l1-1 1.5 1.5-1 1.2C7.5 11 5 8.5 4.4 5.6z" fill="#fff"/></svg>
        <span>08 8412 7395</span>
      </li>
      <li>
        <svg viewBox="0 0 16 16"><rect x="1" y="3.5" width="14" height="9" fill="#fff"/><path d="M1 3.5l7 5 7-5" fill="none" stroke="var(--teal)" stroke-width="1.2"/></svg>
        <span>sales@wexleyhartsa.com.au</span>
      </li>
      <li>
        <svg viewBox="0 0 16 16"><circle cx="8" cy="8" r="7" fill="none" stroke="#fff" stroke-width="1.3"/><ellipse cx="8" cy="8" rx="3" ry="7" fill="none" stroke="#fff" stroke-width="1.1"/><path d="M1 8h14M2.5 4.5h11M2.5 11.5h11" stroke="#fff" stroke-width="1"/></svg>
        <span>wexleyhartsa.com.au</span>
      </li>
    </ul>
  </div>
</body>
</html>
```